Harrowgate Financial Coaching LLC - Needed clean black business card

Business card for personal financial coaching practice located on Las Vegas NV, new startup. Back of card needs to have "how it works" to match the website.

Font styles to use
Sans Serif

Colors

Designer to choose colors to be used in the design.

```html
<!DOCTYPE html>
<html lang="en">
<head>
<meta charset="UTF-8">
<title>Harrowgate Financial Coaching LLC – Business Card</title>
<link rel="stylesheet" href="https://fonts.googleapis.com/css2?family=Montserrat:wght@600;700&family=Arimo:wght@400;700&display=swap">
<style>
  :root {
    --stage: #3a3a3a;
    --card: #0e0e0e;
    --ink: #ffffff;
    --ink-soft: #e6e6e6;
    --rule: #ffffff;
  }
  * { box-sizing: border-box; margin: 0; padding: 0; }
  html, body { width: 1200px; height: 900px; overflow: hidden; }
  body {
    background: var(--stage);
    position: relative;
    font-family: "Arimo", Arial, sans-serif;
    color: var(--ink);
  }
  .card {
    position: absolute;
    width: 720px;
    height: 400px;
    background: var(--card);
    border-radius: 28px;
    box-shadow: 0 14px 30px rgba(0,0,0,.45);
  }
  .card--back { left: 330px; top: 40px; text-align: center; padding: 56px 50px 0; }
  .card--front { left: 150px; top: 470px; }

  .brand {
    font-family: "Montserrat", Arial, sans-serif;
    font-weight: 700;
    text-transform: uppercase;
    color: var(--ink);
    letter-spacing: .5px;
    line-height: 1.15;
  }
  .card--back .brand { font-size: 30px; }
  .brand__sub { display: block; font-size: .72em; letter-spacing: 1px; }

  .how-title {
    margin-top: 34px;
    font-weight: 700;
    font-size: 22px;
    letter-spacing: .5px;
  }
  .how-rule { display: block; margin: 6px auto 0; }
  .how-text {
    margin: 20px auto 0;
    max-width: 600px;
    font-size: 14.5px;
    line-height: 1.65;
    letter-spacing: .6px;
    color: var(--ink-soft);
  }
  .how-link { margin-top: 6px; font-weight: 700; font-size: 15px; letter-spacing: .6px; }

  .card--front .brand {
    position: absolute;
    left: 40px; top: 140px;
    width: 300px;
    font-size: 27px;
    text-align: center;
  }
  .divider {
    position: absolute;
    left: 370px; top: 70px;
    width: 2px; height: 250px;
    background: var(--rule);
  }
  .contact { position: absolute; left: 400px; top: 82px; }
  .contact__name { font-weight: 700; font-size: 25px; letter-spacing: .5px; }
  .contact__role { font-size: 16px; margin-top: 4px; }
  .contact__address { font-size: 16px; line-height: 1.3; margin-top: 12px; }
  .contact__list { list-style: none; margin-top: 12px; font-size: 16px; }
  .contact__list li { display: flex; align-items: center; gap: 8px; line-height: 1.55; }
  .contact__list svg { width: 14px; height: 14px; flex: none; }
</style>
</head>
<body>

<section class="card card--back" aria-label="Card back – How it works">
  <div class="brand">Harrowgate Financial<span class="brand__sub">Coaching LLC</span></div>
  <h2 class="how-title">How It Works</h2>
  <svg class="how-rule" width="240" height="10" viewBox="0 0 240 10" aria-hidden="true">
    <line x1="0" y1="5" x2="240" y2="5" stroke="#fff" stroke-width="1"/>
    <circle cx="120" cy="5" r="3" fill="#fff"/>
  </svg>
  <p class="how-text">All free one-time consultations are in-person meetings only. Paid appointments may be scheduled for in-person or virtual meetings. Select the session, date and time that works best for your schedule. Start your journey of financial freedom at</p>
  <p class="how-link">harrowgatecoaching.com</p>
</section>

<section class="card card--front" aria-label="Card front – Contact details">
  <div class="brand">Harrowgate Financial<span class="brand__sub">Coaching LLC</span></div>
  <div class="divider"></div>
  <div class="contact">
    <div class="contact__name">Grant Harlow</div>
    <div class="contact__role">Manager</div>
    <div class="contact__address">4120 W Desert Sage Ave #305-B<br>Las Vegas, NV 89103</div>
    <ul class="contact__list">
      <li>
        <svg viewBox="0 0 24 24" aria-hidden="true"><path fill="#fff" d="M6.6 10.8a15.1 15.1 0 0 0 6.6 6.6l2.2-2.2a1 1 0 0 1 1-.25 11.4 11.4 0 0 0 3.6.57 1 1 0 0 1 1 1V20a1 1 0 0 1-1 1A17 17 0 0 1 3 4a1 1 0 0 1 1-1h3.5a1 1 0 0 1 1 1c0 1.25.2 2.45.57 3.57a1 1 0 0 1-.25 1z"/></svg>
        702-555-0148
      </li>
      <li>
        <svg viewBox="0 0 24 24" aria-hidden="true"><rect x="2" y="5" width="20" height="14" rx="1" fill="#fff"/><path d="M3 6l9 7 9-7" stroke="#0e0e0e" stroke-width="2" fill="none"/></svg>
        grant@harrowgatecoaching.com
      </li>
      <li>
        <svg viewBox="0 0 24 24" aria-hidden="true"><circle cx="12" cy="12" r="10" fill="#fff"/><path d="M2 12h20M12 2c3 3 3 17 0 20M12 2c-3 3-3 17 0 20" stroke="#0e0e0e" stroke-width="1.5" fill="none"/></svg>
        www.harrowgatecoaching.com
      </li>
    </ul>
  </div>
</section>

</body>
</html>
```